Attorney--Animal Law & Equine Law Litigation & Mediation

Card should read:

Marisol T. R. Quenby, Ph.D., Esq.
Attorney at Law

Back side should reference: Quenby Law Group:
Animal Law, Equine Law, Litigation and Mediation Services

Some small animal-related logo on the back with the above information, showing mixed animals, with a horse in there. Please see samples.

Please see sample cards for front-side view. Something clean and simple. Solid color with text in white. Small logo on front possibly OK.

Can abbreviate Quenby Law Group to QLG

Text also should have address; phone number; website name: www.QuenbyLawGroup.example

Target Market(s)

Attorneys; equine market

Industry/Entity Type

Attorney

Contact Information for Business Card

Marisol T. R. Quenby

Font styles to use
Sans Serif

Colors
0356a4
6b449b

Requirements
Nice to have
• I really like the image I included that has multiple animals, and LAW in big letters. I would change the LAW to QLG (for Quenby Law Group) and then spell out Quenby Law Group under the image perhaps??

```html
<!DOCTYPE html>
<html lang="en">
<head>
<meta charset="utf-8">
<title>Quenby Law Group – Business Card</title>
<link rel="stylesheet" href="https://fonts.googleapis.com/css2?family=Crimson+Text:wght@400;600&display=swap">
<style>
  :root {
    --ink: #0b0b0b;
    --paper: #f1f1f1;
    --paper-shade: #d6d6d6;
    --backdrop: #e6e4df;
    --white: #ffffff;
  }
  * { margin: 0; padding: 0; box-sizing: border-box; }
  html, body { width: 1200px; height: 780px; overflow: hidden; }
  body {
    background: var(--backdrop);
    font-family: "Crimson Text", Georgia, serif;
    position: relative;
  }
  .card {
    position: absolute;
    top: 236px;
    width: 540px;
    height: 308px;
    overflow: hidden;
    box-shadow: 0 6px 18px rgba(0,0,0,.25);
  }
  .card--front { left: 40px; background: linear-gradient(160deg, var(--paper), var(--paper-shade)); }
  .card--back  { left: 620px; background: var(--ink); }

  .rule { position: absolute; left: 0; right: 0; height: 3px; }
  .band { position: absolute; left: 0; right: 0; }

  /* front */
  .card--front .rule { background: var(--ink); }
  .card--front .rule--top { top: 84px; }
  .card--front .band { top: 92px; height: 76px; background: var(--ink); }
  .card--front .rule--bottom { top: 173px; }

  .brand-disc {
    position: absolute;
    border-radius: 50%;
    display: flex; align-items: center; justify-content: center;
    font-size: 16px; font-weight: 600; letter-spacing: 3px;
    text-align: center; line-height: 1.25;
  }
  .card--front .brand-disc {
    left: 205px; top: 65px; width: 130px; height: 130px;
    background: var(--ink); color: var(--white);
    border: 9px solid var(--paper);
  }

  .identity {
    position: absolute; left: 110px; right: 20px; top: 208px;
    text-align: center; color: var(--ink);
  }
  .identity__name { font-size: 24px; font-weight: 600; line-height: 1.15; }
  .identity__title { font-size: 17px; font-weight: 400; line-height: 1.3; }

  /* back */
  .card--back .rule { background: var(--white); }
  .card--back .rule--top { top: 58px; }
  .card--back .band {
    top: 66px; height: 78px;
    background: linear-gradient(180deg, var(--white), #e2e2e2);
  }
  .card--back .rule--bottom { top: 149px; }
  .card--back .brand-disc {
    left: 200px; top: 35px; width: 140px; height: 140px;
    background: var(--white); color: var(--ink);
    border: 14px solid var(--ink);
  }

  .contact {
    position: absolute; left: 20px; right: 20px; top: 182px;
    text-align: center; color: var(--white);
    font-size: 15px; line-height: 1.4;
  }
  .contact__services { font-size: 16px; }
</style>
</head>
<body>
  <section class="card card--front" aria-label="Card front">
    <div class="rule rule--top"></div>
    <div class="band"></div>
    <div class="rule rule--bottom"></div>
    <div class="brand-disc">QUENBY<br>LAW</div>
    <div class="identity">
      <p class="identity__name">Marisol T. R. Quenby, Ph.D., Esq.</p>
      <p class="identity__title">Attorney at Law</p>
    </div>
  </section>

  <section class="card card--back" aria-label="Card back">
    <div class="rule rule--top"></div>
    <div class="band"></div>
    <div class="rule rule--bottom"></div>
    <div class="brand-disc">QUENBY<br>LAW</div>
    <div class="contact">
      <p class="contact__services">Equine Law Animal Law Litigation Mediation</p>
      <p>info@quenbylaw.example</p>
      <p>PO BOX 0000 W. 00 th St., #000 Cedar Ridge, TX 00000 USA</p>
      <p>000-000-0000</p>
      <p>www.QuenbyLawGroup.example</p>
    </div>
  </section>
</body>
</html>
```